Brightkeel Logistics - Cards and Logo

We need a logo and card design for a Logistics company located in Chicago. Our competitors are KTR and Qorvan. We would like to see designs that incorporate a logo that shows all ways in terms of direction. The colors would be Electric Blue, Grays, Blacks and White. I like how Moko has a badge type logo that is strong and clean. Velmora also has a strong font that is futuristic. The final design should communicate we are a strong and technological type of company. I show a picture of the colors we like from a moko cooler.

```html
<!DOCTYPE html>
<html lang="en">
<head>
<meta charset="utf-8">
<title>Brightkeel Logistics – Business Cards</title>
<link rel="stylesheet" href="https://fonts.googleapis.com/css2?family=Oswald:wght@600&family=Work+Sans:wght@400&display=swap">
<style>
  :root {
    --backdrop: #1c1c1d;
    --card: #222223;
    --card-edge: #2c2c2e;
    --electric-blue: #3451b2;
    --silver: #c9c9cc;
    --white: #f4f4f4;
    --rule: #e6e6e6;
  }
  * { box-sizing: border-box; margin: 0; padding: 0; }
  html, body {
    width: 1200px; height: 900px; overflow: hidden;
    background: var(--backdrop);
  }
  .sheet {
    position: relative; width: 1200px; height: 900px;
  }
  .card {
    position: absolute; left: 250px; width: 700px; height: 400px;
    background: linear-gradient(135deg, var(--card) 0%, var(--card-edge) 100%);
    border-radius: 3px;
    box-shadow: 0 12px 30px rgba(0,0,0,0.55);
  }
  .card--brand { top: 40px; display: flex; align-items: center; justify-content: center; }
  .card--contact { top: 470px; display: flex; align-items: center; }

  .wordmark {
    font-family: 'Oswald', sans-serif; font-weight: 600;
    text-transform: uppercase; letter-spacing: 2px; text-align: center;
    line-height: 1.05;
  }
  .card--brand .wordmark { color: var(--silver); font-size: 46px; }

  .contact-logo {
    width: 330px; display: flex; justify-content: center;
  }
  .contact-logo .wordmark { color: var(--white); font-size: 38px; }

  .divider {
    width: 2px; height: 175px; background: var(--rule);
    margin-right: 36px;
  }
  .details { font-family: 'Work Sans', sans-serif; color: var(--white); }
  .details__name {
    font-family: 'Oswald', sans-serif; font-weight: 600;
    color: var(--electric-blue); font-size: 36px; text-transform: uppercase;
    letter-spacing: 0.5px; line-height: 1;
  }
  .details__role { font-size: 17px; margin: 2px 0 16px; }
  .details__address { font-size: 17px; line-height: 1.3; margin-bottom: 6px; }
  .details__line {
    display: flex; align-items: center; gap: 8px;
    font-size: 17px; line-height: 1.35;
  }
  .details__line svg { width: 11px; height: 11px; flex: none; }
  .details__accent { color: var(--electric-blue); }
</style>
</head>
<body>
<main class="sheet">
  <section class="card card--brand">
    <div class="wordmark">Brightkeel<br>Logistics</div>
  </section>

  <section class="card card--contact">
    <div class="contact-logo">
      <div class="wordmark">Brightkeel<br>Logistics</div>
    </div>
    <div class="divider"></div>
    <div class="details">
      <h1 class="details__name">Daniel Reyes</h1>
      <p class="details__role">Director</p>
      <p class="details__address">1184 Harlow Street<br>Lakeport, IL 60412</p>
      <p class="details__line">
        <svg viewBox="0 0 12 12"><path d="M3 1 L5 3.5 L4 4.8 Q5.5 7 7.2 8 L8.5 7 L11 9 L10 11 Q4 10.5 1 2 Z" fill="var(--electric-blue)"/></svg>
        +330 5170-4426
      </p>
      <p class="details__line">
        <svg viewBox="0 0 12 12"><rect x="1" y="2.5" width="10" height="7" fill="none" stroke="var(--electric-blue)" stroke-width="1.2"/><path d="M1 2.5 L6 6.5 L11 2.5" fill="none" stroke="var(--electric-blue)" stroke-width="1.2"/></svg>
        info@brightkeellogistics.com
      </p>
      <p class="details__line">
        <svg viewBox="0 0 12 12"><circle cx="6" cy="6" r="5" fill="none" stroke="var(--electric-blue)" stroke-width="1.2"/><path d="M1 6 H11 M6 1 Q9 6 6 11 Q3 6 6 1" fill="none" stroke="var(--electric-blue)" stroke-width="1"/></svg>
        <span>www.<span class="details__accent">brightkeellogistics</span>.com</span>
      </p>
    </div>
  </section>
</main>
</body>
</html>
```